Goat's Milk Soap

International product development company seeking designs for the following soap label:

Hand crafted in Mt Wattlemere QLD Australia, Carrow Valley
Second Generation Goat Farmers
Soap is hand made in appearance but gives an instant soothing feel when used
High in Vegetable oils and pure fresh goats milk (no powders used)
Give the emotional feel of Quality and Hand crafted
Label must stimulate an emotional response visually
Label must deliver to the customer anticipation for use.
Would anticipate that the label will be produced on a matte finish brown paper label or similar.

Logo should be no larger than 50mm x 50mm
Label should measure around 120mm x 70mm

It Company

```html
<!DOCTYPE html>
<html lang="en">
<head>
<meta charset="utf-8">
<title>Goat's Milk Soap Label</title>
<link rel="stylesheet" href="https://fonts.googleapis.com/css2?family=Pinyon+Script&family=Noto+Sans:wght@400&display=swap">
<style>
  :root {
    --kraft-light: #c99c60;
    --kraft-mid: #b78a50;
    --kraft-dark: #a0743e;
    --ink: #14181b;
    --ornament-tone: rgba(40, 28, 16, 0.32);
    --figure-tone: #1a2226;
    --bubble-tone: #b9c6ce;
    --bubble-shade: #93a3ad;
  }
  html, body {
    margin: 0;
    padding: 0;
    width: 1200px;
    height: 701px;
    overflow: hidden;
    background: #ffffff;
  }
  .label {
    position: relative;
    width: 1200px;
    height: 701px;
    overflow: hidden;
    background:
      radial-gradient(ellipse at 30% 35%, rgba(255,235,190,0.22), transparent 60%),
      radial-gradient(ellipse at 78% 72%, rgba(120,80,30,0.14), transparent 55%),
      linear-gradient(135deg, var(--kraft-light) 0%, var(--kraft-mid) 55%, var(--kraft-dark) 100%);
  }
  .corner-ornament {
    position: absolute;
    width: 160px;
    height: 190px;
    background: radial-gradient(closest-side, var(--ornament-tone), rgba(40,28,16,0.12) 60%, transparent 100%);
  }
  .corner-ornament--top-left { left: 0; top: 0; }
  .corner-ornament--top-right { right: 0; top: 0; }
  .corner-ornament--bottom-left { left: 0; bottom: 0; }
  .corner-ornament--bottom-right { right: 0; bottom: 0; }
  .tagline {
    position: absolute;
    top: 26px;
    left: 0;
    width: 1200px;
    text-align: center;
    font-family: "Pinyon Script", cursive;
    font-size: 64px;
    line-height: 80px;
    color: var(--ink);
    margin: 0;
  }
  .emblem {
    position: absolute;
    left: 407px;
    top: 123px;
    width: 380px;
    height: 316px;
  }
  .emblem__figure {
    position: absolute;
    left: 53px;
    top: 0;
    width: 215px;
    height: 262px;
    border-radius: 50% 50% 24px 24px;
    background: linear-gradient(180deg, var(--figure-tone) 0%, #232d32 100%);
  }
  .emblem__bubbles {
    position: absolute;
    left: 80px;
    top: 214px;
    width: 220px;
    height: 100px;
    border-radius: 50px;
    background: linear-gradient(180deg, var(--bubble-tone) 0%, var(--bubble-shade) 100%);
  }
  .product-name {
    position: absolute;
    top: 472px;
    left: 0;
    width: 1200px;
    text-align: center;
    font-family: "Pinyon Script", cursive;
    font-weight: 400;
    font-size: 124px;
    line-height: 140px;
    color: var(--ink);
    margin: 0;
  }
  .origin {
    position: absolute;
    top: 643px;
    left: 0;
    width: 1200px;
    text-align: center;
    font-family: "Noto Sans", sans-serif;
    font-size: 29px;
    line-height: 40px;
    color: var(--ink);
    margin: 0;
  }
</style>
</head>
<body>
  <main class="label">
    <div class="corner-ornament corner-ornament--top-left" role="img" aria-label="Flourish scroll ornament in dark ink"></div>
    <div class="corner-ornament corner-ornament--top-right" role="img" aria-label="Flourish scroll ornament in dark ink"></div>
    <div class="corner-ornament corner-ornament--bottom-left" role="img" aria-label="Flourish scroll ornament in dark ink"></div>
    <div class="corner-ornament corner-ornament--bottom-right" role="img" aria-label="Flourish scroll ornament in dark ink"></div>

    <p class="tagline">Handmade</p>

    <div class="emblem" role="img" aria-label="Silhouette of a woman blowing soap bubbles, rising from a cloud of pale blue bubbles with ink flourishes">
      <div class="emblem__figure" aria-hidden="true"></div>
      <div class="emblem__bubbles" aria-hidden="true"></div>
    </div>

    <h1 class="product-name">Goat’s Milk Soap</h1>

    <p class="origin">Mt Wattlemere QLD Australia, Carrow Valley</p>
  </main>
</body>
</html>
```